Hi Marlow,

I would like you to design for me a menu board for all my products.

The layout I have hand drawn for you so just follow my layout.

Pho
Noodle salads
Rice
StirFry with Thick Rice Noodles
Spring Rolls Ricepaper Rolls

Poster Size: AO Vertical ( 841W x 1189H)

There are more photos of the rice dishes but I thought I can send this through so you can start and I can send you the rest of the photos when I get back from my photographer.

I will have items descriptions to follow also

Requirements
Must have

```html
<!DOCTYPE html>
<html lang="en">
<head>
<meta charset="UTF-8">
<title>Menu Board</title>
<link href="https://fonts.googleapis.com/css2?family=Cinzel:wght@600&family=Great+Vibes&family=Oswald:wght@500&display=swap" rel="stylesheet">
<style>
  :root {
    --page-bg: #ececec;
    --board-red: #7d0a10;
    --board-dark: #3a0306;
    --gold: #d6a84a;
    --label-gold: #f0c24b;
    --heading-white: #fbf3e6;
    --strip-black: #0d0d0d;
    --photo-dark: #232323;
    --photo-light: #e9e4dc;
  }
  * { box-sizing: border-box; margin: 0; padding: 0; }
  html, body {
    width: 1148px; height: 1200px; overflow: hidden;
    background: var(--page-bg);
  }
  .menu-board {
    position: absolute; left: 164px; top: 20px;
    width: 820px; height: 1160px;
    background: var(--board-red);
    box-shadow: inset 0 0 40px 14px var(--board-dark);
  }
  .board-frame {
    position: absolute; inset: 16px;
    border: 2px solid var(--gold);
  }
  .corner {
    position: absolute; width: 44px; height: 44px;
    background: linear-gradient(135deg, #e2b861, #a87a2c);
  }
  .corner.tl { left: 8px; top: 8px; }
  .corner.tr { right: 8px; top: 8px; }
  .corner.bl { left: 8px; bottom: 8px; }
  .corner.br { right: 8px; bottom: 8px; }
  .board-title {
    position: absolute; left: 78px; top: 12px;
    font-family: "Great Vibes", cursive; font-weight: 400;
    font-size: 44px; line-height: 1; color: var(--heading-white);
  }
  .title-rule {
    position: absolute; left: 190px; right: 66px; top: 52px;
    height: 2px; background: var(--gold);
  }
  .menu-sections {
    position: absolute; left: 0; right: 0; top: 74px;
    display: flex; flex-direction: column; align-items: center;
  }
  .section-heading {
    font-family: "Cinzel", serif; font-weight: 600;
    font-size: 28px; line-height: 34px; letter-spacing: 1px;
    color: var(--heading-white); margin: 8px 0 6px;
    white-space: nowrap;
  }
  .dish-strip { display: flex; flex-direction: column; }
  .dish-photos { display: flex; gap: 4px; }
  .dish-photo {
    background: radial-gradient(ellipse 48% 42% at 50% 52%, var(--photo-light) 0 55%, #9c8a70 62%, var(--photo-dark) 72%);
  }
  .dish-labels {
    display: flex; background: var(--strip-black);
    margin-top: 6px; height: 36px; align-items: center;
  }
  .dish-label {
    flex: 1; text-align: center;
    font-family: "Oswald", sans-serif; font-weight: 500;
    font-size: 15px; line-height: 1; color: var(--label-gold);
    text-transform: uppercase; transform: scaleX(0.85);
    white-space: nowrap;
  }
  .pho .dish-photo { width: 150px; height: 120px; }
  .salads .dish-photo { width: 140px; height: 104px; }
  .rice .dish-photo { width: 140px; height: 100px; }
  .stirfry .dish-photo { width: 146px; height: 100px; }
  .rolls .dish-photo { width: 146px; height: 118px; }
  .stirfry, .rolls { margin-left: 80px; }
</style>
</head>
<body>
  <main class="menu-board">
    <div class="board-frame"></div>
    <div class="corner tl" role="img" aria-label="Gold corner ornament"></div>
    <div class="corner tr" role="img" aria-label="Gold corner ornament"></div>
    <div class="corner bl" role="img" aria-label="Gold corner ornament"></div>
    <div class="corner br" role="img" aria-label="Gold corner ornament"></div>
    <h1 class="board-title">Menu</h1>
    <div class="title-rule"></div>

    <div class="menu-sections">
      <h2 class="section-heading">PHO</h2>
      <section class="dish-strip pho">
        <div class="dish-photos">
          <div class="dish-photo" role="img" aria-label="Bowl of beef pho"></div>
          <div class="dish-photo" role="img" aria-label="Bowl of chicken pho"></div>
          <div class="dish-photo" role="img" aria-label="Bowl of tofu pho"></div>
        </div>
        <div class="dish-labels">
          <span class="dish-label">Beef Pho</span>
          <span class="dish-label">Chicken Pho</span>
          <span class="dish-label">Tofu Pho</span>
        </div>
      </section>

      <h2 class="section-heading">NOODLE SALADS</h2>
      <section class="dish-strip salads">
        <div class="dish-photos">
          <div class="dish-photo" role="img" aria-label="Beef noodle salad"></div>
          <div class="dish-photo" role="img" aria-label="Chicken noodle salad"></div>
          <div class="dish-photo" role="img" aria-label="Chicken noodle salad"></div>
          <div class="dish-photo" role="img" aria-label="BBQ pork noodle salad"></div>
        </div>
        <div class="dish-labels">
          <span class="dish-label">Beef Noodle Salad</span>
          <span class="dish-label">Chiken Noodle Salad</span>
          <span class="dish-label">Chiken Noodle Salad</span>
          <span class="dish-label">BBQ Pork Noodle Salad</span>
        </div>
      </section>

      <h2 class="section-heading">RICE</h2>
      <section class="dish-strip rice">
        <div class="dish-photos">
          <div class="dish-photo" role="img" aria-label="Beef with rice"></div>
          <div class="dish-photo" role="img" aria-label="Chicken with rice"></div>
          <div class="dish-photo" role="img" aria-label="Tofu with rice"></div>
          <div class="dish-photo" role="img" aria-label="Fried rice pho"></div>
        </div>
        <div class="dish-labels">
          <span class="dish-label">Beef With Rice</span>
          <span class="dish-label">Chicken With Rice</span>
          <span class="dish-label">Tofu With Rice</span>
          <span class="dish-label">Fried Rice Pho</span>
        </div>
      </section>

      <h2 class="section-heading">STIR FRY WITH THICK RICE NOODLES</h2>
      <section class="dish-strip stirfry">
        <div class="dish-photos">
          <div class="dish-photo" role="img" aria-label="Stir fry noodles with beef"></div>
          <div class="dish-photo" role="img" aria-label="Stir fry noodles with chicken"></div>
          <div class="dish-photo" role="img" aria-label="Stir fry noodles with tofu"></div>
        </div>
        <div class="dish-labels">
          <span class="dish-label">Stir Fry Noodles Beef</span>
          <span class="dish-label">Stir Fry Noodles Chicken</span>
          <span class="dish-label">Stir Fry Noodles Tofu</span>
        </div>
      </section>

      <h2 class="section-heading">SPRING ROLLS RICEPAPER ROLLS</h2>
      <section class="dish-strip rolls">
        <div class="dish-photos">
          <div class="dish-photo" role="img" aria-label="Fried spring rolls with dipping sauce"></div>
          <div class="dish-photo" role="img" aria-label="Fresh ricepaper rolls on a board"></div>
        </div>
        <div class="dish-labels">
          <span class="dish-label">Spring Rolls</span>
          <span class="dish-label">Ricepaper Rolls</span>
        </div>
      </section>
    </div>
  </main>
</body>
</html>
```